Business card Zottelgarten

Business card is for a self-employed dog trainer with own dog school. Name and logo of the dog school are available. Color specifications as well. The design should be classy and minimalist, but also modern. An already existing idea would be: Front: Only the logo Back: Contact data

Font styles to use
Serif
Sans Serif
Other font styles liked:
• Trajan Pro

Colors
f78f20

Requirements
Must have
• Name: Margit Wendler-Rasch Title: Dipl. Dog Trainer Contain my logo Follow my font and color preferences (see files)

```html
<!DOCTYPE html>
<html lang="de">
<head>
<meta charset="utf-8">
<title>Zottelgarten – Business Card</title>
<link rel="stylesheet" href="https://fonts.googleapis.com/css2?family=Cinzel:wght@400;500&display=swap">
<style>
  :root {
    --page-bg: #e6e6e8;
    --card-brown: #7d6a5a;
    --card-orange: #f78f20;
    --ink-light: #ffffff;
    --type: "Cinzel", "Trajan Pro", serif;
  }
  * { box-sizing: border-box; margin: 0; padding: 0; }
  html, body {
    width: 1200px; height: 1200px; overflow: hidden;
    background: var(--page-bg);
    font-family: var(--type);
    color: var(--ink-light);
  }
  .card {
    position: absolute;
    left: 237px; width: 727px; height: 416px;
  }
  .card--front { top: 148px; background: var(--card-brown); }
  .card--back  { top: 652px; background: var(--card-orange); }

  .front-mark {
    position: absolute; left: 221px; top: 30px;
    width: 284px; height: 284px;
  }
  .front-name {
    position: absolute; left: 0; right: 0; top: 320px;
    text-align: center;
    font-size: 64px; font-weight: 400;
    letter-spacing: 6px; line-height: 1;
    white-space: nowrap;
  }

  .print-area {
    position: absolute; left: 4px; top: 12px;
    width: 220px; height: 400px;
  }
  .back-mark {
    position: absolute; left: 595px; top: 26px;
    width: 64px; height: 64px;
  }
  .back-brand {
    position: absolute; left: 551px; top: 94px;
    font-size: 17.5px; font-weight: 400;
    letter-spacing: 1.4px; line-height: 1;
    white-space: nowrap;
  }
  .holder {
    position: absolute; left: 243px; top: 190px;
    text-align: center;
    white-space: nowrap;
  }
  .holder-name {
    font-size: 33px; font-weight: 400;
    letter-spacing: 1.2px; line-height: 1;
  }
  .holder-title {
    margin-top: 8px;
    font-size: 22px; font-weight: 400;
    letter-spacing: 1px; line-height: 1;
  }
  .contact {
    position: absolute; left: 241px; top: 350px;
    font-size: 17.5px; font-weight: 400;
    letter-spacing: 0.6px; line-height: 1;
    white-space: nowrap;
  }
</style>
</head>
<body>
  <section class="card card--front" aria-label="Card front">
    <svg class="front-mark" viewBox="0 0 284 284" aria-hidden="true">
      <circle cx="142" cy="142" r="139" fill="none" stroke="#ffffff" stroke-width="3"/>
      <circle cx="142" cy="142" r="132" fill="#ffffff"/>
    </svg>
    <h1 class="front-name">Zottelgarten</h1>
  </section>

  <section class="card card--back" aria-label="Card back">
    <svg class="print-area" viewBox="0 0 220 400" role="img" aria-label="White illustration of a dog paw print merging into a human hand print with a heart in the palm">
      <defs>
        <radialGradient id="printFill" cx="50%" cy="45%" r="60%">
          <stop offset="0%" stop-color="#ffffff"/>
          <stop offset="100%" stop-color="#ffffff" stop-opacity="0.75"/>
        </radialGradient>
      </defs>
      <ellipse cx="115" cy="200" rx="100" ry="190" fill="url(#printFill)"/>
    </svg>

    <svg class="back-mark" viewBox="0 0 64 64" aria-hidden="true">
      <circle cx="32" cy="32" r="31" fill="#ffffff"/>
    </svg>
    <div class="back-brand">Zottelgarten</div>

    <div class="holder">
      <h2 class="holder-name">Margit Wendler-Rasch</h2>
      <p class="holder-title">Dipl. Dog Trainer</p>
    </div>

    <p class="contact">Tel: (123) 456-7890 | Web: zottelgarten.ch</p>
  </section>
</body>
</html>
```